Einfache Webside für kleine Promotion- und Personalagentur
Eine aussergewöhnlich kreative und nette Designerin - die sehr, sehr geduldig mit mir war :-)
Zielgruppe
Falkwerk Personal ist eine international tätige Promotion- und Personalagentur. Wir bieten auch im Bereich Sport der jew. Sportart affine Hostessen und Hosts f an.
Aufgabenstellung
Wir hatten bis dato eine sehr gute Auftragslage und leider keine Zeit für eine Homepage. Wir suchen jemaden der uns das Design für die Seite übernimmt und Online stellt. Wir sind auch offen wenn dies über z.B. Q7+ erfolgt. Auf den jeweiligen Seiten wollen wir den Text dann immer selbst eintragen. Seiten: Startseite mit Buttons zu folgenden Feldern: Promotion (Text mit Erklärung was wir machen und Bildern), Personal (Text mit Erklärung was wir machen und Bilder - die Bilder sollten austauschbar sein), Team, Referenzen, Kontaktseite, Gästebuch, Impressum. Die Seite sollte Modern aussehen und nicht zu überladen sein.

```html
<!DOCTYPE html>
<html lang="de">
<head>
<meta charset="utf-8">
<title>Falkwerk Personal – International Promotion &amp; HR Services</title>
<link rel="stylesheet" href="https://fonts.googleapis.com/css2?family=Arimo:wght@400;700&family=Catamaran:wght@300;400;600;700&display=swap">
<style>
  :root {
    --teal: #7ccad4;
    --teal-dark: #2f5f6a;
    --ink: #1b2631;
    --ring: #8a99a3;
    --text: #111;
    --white: #fff;
    --footer-grey: #a6adb2;
    --hero-top: #e4ebef;
    --hero-bottom: #a9b8c0;
  }
  * { box-sizing: border-box; margin: 0; padding: 0; }
  html, body { width: 1200px; height: 1067px; overflow: hidden; }
  body { position: relative; background: var(--white); font-family: "Catamaran", sans-serif; color: var(--text); }

  .hero {
    position: absolute; left: 0; top: 0; width: 1200px; height: 264px;
    background: radial-gradient(ellipse at 25% 30%, #f6f9fa 0%, transparent 45%),
                linear-gradient(180deg, var(--hero-top) 0%, var(--hero-bottom) 100%);
  }
  .brand { position: absolute; left: 0; top: 150px; width: 1200px; text-align: center; }
  .brand-name { font-family: "Catamaran", sans-serif; font-weight: 700; font-size: 40px; color: var(--teal-dark); line-height: 1; }
  .brand-tagline { font-family: "Catamaran", sans-serif; font-size: 16px; color: #34434d; margin-top: 6px; }
  .brand-dot { position: absolute; left: 553px; top: 50px; width: 96px; height: 96px; border-radius: 50%; background: var(--teal-dark); }

  .lang {
    position: absolute; right: 0; top: 17px; width: 99px; height: 32px;
    background: var(--teal); display: flex; align-items: center; justify-content: space-around;
    font-family: "Arimo", sans-serif; font-size: 16px; color: var(--ink);
  }

  .nav { position: absolute; left: 0; top: 264px; width: 1200px; height: 42px; background: var(--teal); }
  .nav-badge { position: absolute; left: 100px; top: -20px; width: 84px; height: 84px; border-radius: 50%; background: var(--white); }
  .nav a {
    position: absolute; top: 10px; font-family: "Arimo", sans-serif; font-weight: 700;
    font-size: 17px; letter-spacing: 1.2px; color: var(--ink); text-decoration: none;
  }

  .service { position: absolute; top: 370px; width: 330px; text-align: center; }
  .service h2 { font-family: "Arimo", sans-serif; font-weight: 700; font-size: 20px; color: var(--ink); }
  .service-visual { position: relative; width: 220px; height: 220px; margin: 20px auto 0; }
  .service-visual svg { position: absolute; left: 0; top: 0; }
  .service-text { position: absolute; top: 277px; width: 252px; font-size: 12.8px; line-height: 15px; }
  .service-text .line { display: block; white-space: nowrap; text-align: justify; text-align-last: justify; }
  .service-text .line.end { text-align-last: left; }
  .service-text .gap { display: block; height: 15px; }
  .more {
    position: absolute; top: 383px; width: 120px; height: 24px; border-radius: 12px; background: var(--teal);
    color: var(--white); font-weight: 700; font-size: 14px; letter-spacing: .5px;
    display: flex; align-items: center; gap: 6px; padding-left: 6px; text-decoration: none;
  }

  .social { position: absolute; top: 853px; width: 28px; height: 28px; border-radius: 50%; background: var(--ink); }
  .footer-links { position: absolute; right: 125px; top: 856px; font-size: 15px; color: var(--ink); display: flex; align-items: center; gap: 9px; }

  .footer { position: absolute; left: 0; top: 899px; width: 1200px; height: 168px; background: var(--ink); color: #e8edf0; font-weight: 300; font-size: 12.5px; line-height: 16px; }
  .footer-col { position: absolute; top: 52px; }
  .footer-rule { position: absolute; top: 49px; width: 2px; height: 80px; background: var(--teal); }
  .footer-name { position: absolute; right: 129px; top: 78px; font-family: "Catamaran", sans-serif; font-weight: 400; font-size: 16px; line-height: 20px; color: var(--footer-grey); }
</style>
</head>
<body>

<header class="hero" role="img" aria-label="Unscharfes Foto von Geschäftsleuten in Silhouette">
  <div class="brand-dot"></div>
  <div class="brand">
    <div class="brand-name">Falkwerk Personal</div>
    <div class="brand-tagline">International Promotion &amp; HR services</div>
  </div>
  <div class="lang"><span>DE</span><span>I</span><span>EN</span></div>
</header>

<nav class="nav">
  <div class="nav-badge"></div>
  <a style="left:248px">SERVICES</a>
  <a style="left:399px">TEAM</a>
  <a style="left:512px">REFERENZEN</a>
  <a style="left:695px">KONTAKT</a>
  <a style="left:841px">IMPRESSUM</a>
  <a style="left:1010px">SUCHE</a>
</nav>

<section class="service" style="left:110px">
  <h2>PROMOTION</h2>
  <div class="service-visual">
    <svg width="220" height="220" viewBox="0 0 220 220">
      <circle cx="110" cy="110" r="100" fill="none" stroke="var(--ring)" stroke-width="10" stroke-dasharray="560 68" transform="rotate(-10 110 110)"/>
      <circle cx="110" cy="110" r="88" fill="#c79a72" role="img" aria-label="Foto einer Promoterin mit Flyern"/>
    </svg>
  </div>
  <div class="service-text" style="left:32px">
    <span class="line">Lorem ipsum dolor sit amet, consectetuer</span>
    <span class="line">adipiscing elit. Aenean commodo ligula eget</span>
    <span class="line end">dolor.</span>
    <span class="gap"></span>
    <span class="line">Aenean massa. Cum sociis natoque penati-</span>
    <span class="line">bus et magnis dis parturient montes, nasce-</span>
  </div>
  <a class="more" style="left:97px"><svg width="16" height="16" viewBox="0 0 16 16"><circle cx="8" cy="8" r="7.5" fill="#5a7a84"/><path d="M5 8h6M8.5 5l3 3-3 3" stroke="#fff" stroke-width="1.6" fill="none"/></svg>MEHR INFOS</a>
</section>

<section class="service" style="left:441px">
  <h2>HR-SERVICE</h2>
  <div class="service-visual">
    <svg width="220" height="220" viewBox="0 0 220 220">
      <circle cx="110" cy="110" r="100" fill="none" stroke="var(--ring)" stroke-width="10" stroke-dasharray="560 68" transform="rotate(-10 110 110)"/>
      <circle cx="110" cy="110" r="88" fill="#b08a68" role="img" aria-label="Porträtfoto einer Personalberaterin"/>
    </svg>
  </div>
  <div class="service-text" style="left:50px">
    <span class="line">Lorem ipsum dolor sit amet, consectetuer</span>
    <span class="line">adipiscing elit. Aenean commodo ligula eget</span>
    <span class="line end">dolor.</span>
    <span class="gap"></span>
    <span class="line">Aenean massa. Cum sociis natoque penati-</span>
    <span class="line">bus et magnis dis parturient montes, nasce-</span>
  </div>
  <a class="more" style="left:115px"><svg width="16" height="16" viewBox="0 0 16 16"><circle cx="8" cy="8" r="7.5" fill="#5a7a84"/><path d="M5 8h6M8.5 5l3 3-3 3" stroke="#fff" stroke-width="1.6" fill="none"/></svg>MEHR INFOS</a>
</section>

<section class="service" style="left:772px">
  <h2>SPORT PROMOTION</h2>
  <div class="service-visual">
    <svg width="220" height="220" viewBox="0 0 220 220">
      <circle cx="110" cy="110" r="100" fill="none" stroke="var(--ring)" stroke-width="10" stroke-dasharray="560 68" transform="rotate(-10 110 110)"/>
      <circle cx="110" cy="110" r="88" fill="#a9c2cb" role="img" aria-label="Foto von zwei Surfern am Strand"/>
    </svg>
  </div>
  <div class="service-text" style="left:41px">
    <span class="line">Lorem ipsum dolor sit amet, consectetuer</span>
    <span class="line">adipiscing elit. Aenean commodo ligula eget</span>
    <span class="line end">dolor.</span>
    <span class="gap"></span>
    <span class="line">Aenean massa. Cum sociis natoque penati-</span>
    <span class="line">bus et magnis dis parturient montes, nasce-</span>
  </div>
  <a class="more" style="left:105px"><svg width="16" height="16" viewBox="0 0 16 16"><circle cx="8" cy="8" r="7.5" fill="#5a7a84"/><path d="M5 8h6M8.5 5l3 3-3 3" stroke="#fff" stroke-width="1.6" fill="none"/></svg>MEHR INFOS</a>
</section>

<a class="social" style="left:129px" aria-label="Soziales Netzwerk"></a>
<a class="social" style="left:164px" aria-label="Berufsnetzwerk"></a>

<div class="footer-links">
  <span>Kontakt</span><span>|</span><span>Impressum</span><span>|</span>
  <svg width="14" height="14" viewBox="0 0 14 14"><circle cx="5.5" cy="5.5" r="4.2" fill="none" stroke="var(--ink)" stroke-width="2"/><path d="M8.6 8.6L13 13" stroke="var(--ink)" stroke-width="2.4"/></svg>
</div>

<footer class="footer">
  <div class="footer-col" style="left:254px">Falkwerk Personal<br>International Promotion &amp; HR Services<br>Geschäftsführer: Katrin Mollenhauer</div>
  <div class="footer-rule" style="left:469px"></div>
  <div class="footer-col" style="left:481px">Am Kiefernhang 12<br>83071 Sternbach</div>
  <div class="footer-rule" style="left:612px"></div>
  <div class="footer-col" style="left:621px">Tel.: +49 (0) 80 31 40 22 19 6<br>E-Mail: kontakt@falkwerk-personal.de<br>www.falkwerk-personal.de</div>
  <div class="footer-rule" style="left:816px"></div>
  <div class="footer-name">Falkwerk Personal</div>
</footer>

</body>
</html>
```